Business Card Design

We need a business card for a well established Semi Trailer Hire company. I am looking for a new start as we are moving so would like to update our Business Cards and Letter heads.
We hire Semi Trailers to Transport companies.
The colour of our Trailers are Cherry Red so this must be the prominent colour.
I do not want any pictures of trailers on the design.
I do not want the design to be flowery in anyway as we are in the transport industry.
Simple yet effective

Business

Varno Tolt Hire Pty Ltd
Ros Penbury
Director
Ph: 03 9412 5038
Mobile: 0427 836 207
ros.penbury@varnotolt-example.com.au
www.varnotolt-example.com.au
218-224 Dunmore Road, Yarraville

```html
<!DOCTYPE html>
<html lang="en">
<head>
<meta charset="utf-8">
<title>Varno Tolt Hire – Business Card</title>
<link rel="stylesheet" href="https://fonts.googleapis.com/css2?family=Arimo:wght@400&family=PT+Sans+Narrow:wght@400&family=Philosopher:wght@700&display=swap">
<style>
  :root {
    --cherry: #b21d24;
    --lemon: #ebe84f;
    --paper: #ffffff;
    --ink: #111111;
    --backdrop: #e9e9e9;
    --card-w: 880px;
    --card-h: 500px;
  }
  * { box-sizing: border-box; margin: 0; padding: 0; }
  html, body {
    width: 1100px;
    height: 1200px;
    overflow: hidden;
    background: var(--backdrop);
  }
  .canvas {
    width: 1100px;
    height: 1200px;
    display: flex;
    flex-direction: column;
    align-items: center;
    justify-content: center;
    gap: 60px;
  }
  .card {
    position: relative;
    width: var(--card-w);
    height: var(--card-h);
    background: var(--paper);
    overflow: hidden;
    box-shadow: 0 4px 14px rgba(0,0,0,0.18);
  }
  .card-shapes {
    position: absolute;
    inset: 0;
    width: 100%;
    height: 100%;
  }
  .shape-lemon { fill: var(--lemon); }
  .shape-cherry { fill: var(--cherry); }
  .shape-paper { fill: var(--paper); }
  .shape-rule { fill: var(--ink); }

  /* Front */
  .company-name {
    position: absolute;
    top: 112px;
    left: 0;
    width: 100%;
    text-align: center;
    font-family: "PT Sans Narrow", sans-serif;
    font-size: 60px;
    color: var(--cherry);
    letter-spacing: 0.5px;
  }
  .front-email {
    position: absolute;
    top: 402px;
    left: 0;
    width: 100%;
    text-align: center;
    font-family: "Arimo", sans-serif;
    font-size: 22px;
    color: var(--cherry);
  }

  /* Back */
  .person {
    position: absolute;
    top: 100px;
    right: 90px;
    text-align: right;
    color: var(--paper);
    font-family: "Philosopher", serif;
    font-weight: 700;
  }
  .person-name {
    font-size: 56px;
    line-height: 1;
    letter-spacing: 1px;
  }
  .person-role {
    font-size: 34px;
    line-height: 1;
    margin-right: 60px;
    letter-spacing: 1px;
  }
  .contact {
    position: absolute;
    top: 318px;
    left: 515px;
    width: 350px;
    text-align: center;
    color: var(--paper);
    font-family: "Arimo", sans-serif;
    font-size: 22px;
    line-height: 42px;
    letter-spacing: 1.5px;
    list-style: none;
  }
  .web-address {
    position: absolute;
    left: 48px;
    bottom: 34px;
    font-family: "Arimo", sans-serif;
    font-size: 21px;
    color: var(--cherry);
  }
</style>
</head>
<body>
<main class="canvas">

  <section class="card card-front" aria-label="Business card front">
    <svg class="card-shapes" viewBox="0 0 880 500" preserveAspectRatio="none" aria-hidden="true">
      <path class="shape-rule" d="M0,210 C300,335 650,325 880,250 L880,262 C650,338 300,348 0,222 Z"/>
      <path class="shape-lemon" d="M0,0 H880 V248 C650,322 300,330 0,206 Z"/>
    </svg>
    <h1 class="company-name">VARNO TOLT HIRE PTY LTD</h1>
    <p class="front-email">ros.penbury@varnotolt-example.com.au</p>
  </section>

  <section class="card card-back" aria-label="Business card back">
    <svg class="card-shapes" viewBox="0 0 880 500" preserveAspectRatio="none" aria-hidden="true">
      <rect class="shape-lemon" x="0" y="0" width="880" height="500"/>
      <path class="shape-paper" d="M240,0 C310,90 330,260 385,390 C415,455 450,488 490,500 L880,500 L880,0 Z"/>
      <path class="shape-cherry" d="M250,0 C335,80 365,250 420,380 C450,450 480,482 525,500 L880,500 L880,0 Z"/>
    </svg>
    <div class="person">
      <h2 class="person-name">Ros Penbury</h2>
      <p class="person-role">Director</p>
    </div>
    <ul class="contact">
      <li class="contact-address">218-224 Dunmore Road, Yarraville</li>
      <li class="contact-phone">03 9412 5038</li>
      <li class="contact-mobile">0427 836 207</li>
    </ul>
    <p class="web-address">www.varnotolt-example.com.au</p>
  </section>

</main>
</body>
</html>
```